Letterhead for New Orthopaedic Surgery Practice

My husband and I are starting our own practice named RB Spine & Vitality Center. We would like to create a nice simple but high class letterhead that doesn't use too much solid color ink when printing. I like the colors dark blue, gold, yellow. Open to other suggestions. We will need to list him and I both on the top of the letterhead. Here is the important information:
Lucinda Perrow, M.D. - Hand and Upper Extremity Surgery
Abena Quist, M.D. - Hip & Knee Replacement/General Orthopaedic Surgery
Location: 18735 North Harlow Pkwy
Coral Springs, FL 33071
Phone: 954-218-4650
Fax: 954-582-1346
Email: info@myrbspine.com

The only thing is that the phone and fax numbers will change once we get into our space. I just want to get the design started. I am including several documents which are my previous practice letterhead, my current procedure room letterhead, and our new Logo. The other letterheads are just for examples but please think outside of the box! We would love to see some great designs.

Colors
0054AA
0677BA
7BADD7
CADEEF
E8F1F8
0094D4
00A9DD
6FCCEA
C7EBF8
E9F6FB

Requirements
Must have
• class, elegance, luxury

```html
<!DOCTYPE html>
<html lang="en">
<head>
<meta charset="utf-8">
<title>RB Spine &amp; Vitality Center — Letterhead</title>
<link rel="stylesheet" href="https://fonts.googleapis.com/css2?family=Poppins:wght@500;600;700&display=swap">
<style>
  :root {
    --navy: #1c2a52;
    --gold: #c9a45c;
    --paper: #ffffff;
    --backdrop: #e6e6e9;
    --watermark: #ececec;
  }
  * { margin: 0; padding: 0; box-sizing: border-box; }
  html, body {
    width: 1200px; height: 799px; overflow: hidden;
    background: var(--backdrop);
    font-family: "Poppins", sans-serif;
  }
  .letterhead {
    position: absolute; left: 331px; top: 20px;
    width: 538px; height: 760px;
    background: var(--paper);
    box-shadow: 0 2px 10px rgba(0,0,0,.12);
  }
  .physician { position: absolute; top: 36px; }
  .physician--left { left: 37px; }
  .physician--right { left: 362px; top: 33px; }
  .physician__name {
    color: var(--navy); font-weight: 700; font-size: 12.5px; line-height: 1.2;
  }
  .physician__specialty {
    color: var(--gold); font-weight: 600; font-size: 7.6px; line-height: 1.3;
  }
  .brand-mark {
    position: absolute; left: 232px; top: 20px;
    width: 74px; height: 74px; border: 1.2px solid var(--navy); border-radius: 50%;
    display: flex; align-items: center; justify-content: center; text-align: center;
    color: var(--navy); font-weight: 600; font-size: 8.4px; line-height: 1.25;
  }
  .brand-watermark {
    position: absolute; left: 172px; top: 290px;
    width: 195px; height: 195px; border: 2px solid var(--watermark); border-radius: 50%;
    display: flex; align-items: center; justify-content: center; text-align: center;
    color: var(--watermark); font-weight: 600; font-size: 22px; line-height: 1.2;
  }
  .footer-rule {
    position: absolute; left: 28px; top: 699px; width: 485px; height: 2px;
    background: var(--gold);
  }
  .contact {
    position: absolute; left: 0; width: 100%;
    display: flex; justify-content: center; align-items: center; gap: 5px;
    color: var(--navy); font-weight: 600; font-size: 9px;
  }
  .contact--address { top: 712px; }
  .contact--lines { top: 730px; }
  .contact__item { display: flex; align-items: center; gap: 4px; }
  .contact__icon { width: 13px; height: 13px; flex: none; }
</style>
</head>
<body>
  <main class="letterhead">
    <header>
      <div class="physician physician--left">
        <p class="physician__name">Lucinda Perrow, M.D.</p>
        <p class="physician__specialty">Hand and Upper Extremity Surgery</p>
      </div>
      <div class="brand-mark">RB Spine &amp;<br>Vitality<br>Center</div>
      <div class="physician physician--right">
        <p class="physician__name">Abena Quist, M.D.</p>
        <p class="physician__specialty">Hip &amp; Knee Replacement<br>General Orthopaedic Surgery</p>
      </div>
    </header>

    <div class="brand-watermark" aria-hidden="true">RB Spine &amp;<br>Vitality<br>Center</div>

    <footer>
      <div class="footer-rule"></div>
      <p class="contact contact--address">
        <span class="contact__item">
          <svg class="contact__icon" viewBox="0 0 14 14"><circle cx="7" cy="7" r="7" fill="var(--gold)"/><path d="M7 3.2a2.5 2.5 0 0 0-2.5 2.5c0 1.9 2.5 4.8 2.5 4.8s2.5-2.9 2.5-4.8A2.5 2.5 0 0 0 7 3.2z" fill="#fff"/><circle cx="7" cy="5.7" r=".9" fill="var(--gold)"/></svg>
          18735 North Harlow Pkwy, Coral Springs, FL 33071
        </span>
      </p>
      <p class="contact contact--lines">
        <span class="contact__item">
          <svg class="contact__icon" viewBox="0 0 14 14"><circle cx="7" cy="7" r="7" fill="var(--gold)"/><path d="M4.6 3.6l1.3-.3.8 1.8-.9.7c.4.9 1.1 1.6 2 2l.7-.9 1.8.8-.3 1.3c-3 .3-5.7-2.4-5.4-5.4z" fill="#fff"/></svg>
          954-218-4650
        </span>
        <span class="contact__item">
          <svg class="contact__icon" viewBox="0 0 14 14"><circle cx="7" cy="7" r="7" fill="var(--gold)"/><rect x="4.8" y="3.3" width="4.4" height="2.2" fill="#fff"/><rect x="3.5" y="5.8" width="7" height="3.4" rx=".6" fill="#fff"/><rect x="4.8" y="8.4" width="4.4" height="2.3" fill="#fff" stroke="var(--gold)" stroke-width=".5"/></svg>
          954-582-1346
        </span>
        <span class="contact__item">
          <svg class="contact__icon" viewBox="0 0 14 14"><circle cx="7" cy="7" r="7" fill="var(--gold)"/><rect x="3.6" y="4.6" width="6.8" height="4.8" rx=".5" fill="#fff"/><path d="M3.8 4.9L7 7.3l3.2-2.4" fill="none" stroke="var(--gold)" stroke-width=".7"/></svg>
          info@myrbspine.com
        </span>
      </p>
    </footer>
  </main>
</body>
</html>
```